Brightfold Partners Website

Brightfold Partners Advisory Services is a company which provides specialised advise in carbon markets, climate policy, landscapes, resilience and change. We are based in Australia but the majority of our business is global. Our clients range from governments to large corporates and not for profit organisations.
Our focus is on developing the capabilities of government officials, business decision makers and land managers so they can better navigate the complexity of climate change and sustainability.
We are looking for a website that is consistent with the high end professional services which we provide to serious players.
I have attached two versions of our logo. I have also attached the back of our business card so you can get a sense of what we hand to potential clients.

Target Market(s)

Professional individuals, decision makers, board members etc, government officials.

Industry/Entity Type

Government

Number of Pages Required

4 page

Font styles to use
Serif
Sans Serif

Requirements
Must have
• Please provide
• 1. Home page
• 2. Service page template
• 3. Contact page
• 4. Lead expert profile page

```html
<!DOCTYPE html>
<html lang="en">
<head>
<meta charset="utf-8">
<title>Brightfold Partners – People</title>
<link href="https://fonts.googleapis.com/css2?family=Cinzel:wght@400;600&family=Open+Sans:wght@400;600&family=Lato:wght@400&family=Crimson+Text:wght@400&display=swap" rel="stylesheet">
<style>
  :root {
    --blue: #2383cc;
    --blue-text: #3a8fd0;
    --ink: #333;
    --grey: #555;
    --rule: #d3d5da;
    --bar: #2b2b2b;
    --page: #eceef2;
    --page-light: #f4f5f8;
    --white: #fff;
  }
  * { margin: 0; padding: 0; box-sizing: border-box; }
  html, body { width: 891px; height: 1200px; overflow: hidden; }
  body {
    position: relative;
    font-family: "Open Sans", sans-serif;
    color: var(--ink);
    background: radial-gradient(ellipse 60% 70% at 50% 40%, var(--page-light), var(--page) 70%, #dfe1e6);
  }
  .top-bar { position: absolute; left: 0; top: 0; width: 891px; height: 8px; background: var(--bar); }

  /* Header */
  .brand { position: absolute; left: 113px; top: 38px; display: flex; align-items: center; gap: 11px; }
  .brand-dot { width: 50px; height: 50px; border-radius: 50%; background: #8a8d92; }
  .brand-name { font-family: "Cinzel", serif; font-weight: 400; font-size: 24px; line-height: 28px; letter-spacing: 1px; color: #3c3d40; white-space: nowrap; }
  .call { position: absolute; right: 113px; top: 36px; display: flex; align-items: center; gap: 8px; }
  .call-label { font-size: 14px; color: var(--grey); }
  .call-number { font-family: "Crimson Text", serif; font-size: 19px; color: var(--blue-text); margin-left: -4px; }
  .main-nav { position: absolute; top: 76px; right: 113px; display: flex; gap: 22px; align-items: center; font-size: 10px; color: #444; }
  .main-nav a { color: inherit; text-decoration: none; padding: 3px 0; }
  .main-nav a.active { background: var(--blue); color: var(--white); border: 1px solid #14578a; border-radius: 3px; padding: 3px 7px; }

  /* Slider */
  .slider { position: absolute; left: 113px; top: 126px; width: 665px; height: 276px; background: var(--white); box-shadow: 0 0 4px rgba(0,0,0,.12); }
  .slide-image { position: absolute; left: 7px; top: 7px; width: 650px; height: 262px;
    background: linear-gradient(100deg, #d8dadb 0%, #b8bcc0 35%, #7c8590 60%, #3e4650 80%, #5b6874 100%); }
  .slide-caption { position: absolute; left: 7px; bottom: 7px; width: 650px; height: 27px; background: rgba(15,18,22,.85);
    font-family: "Cinzel", serif; font-weight: 600; font-size: 13.5px; color: var(--white); text-align: center; line-height: 27px; letter-spacing: .3px; }
  .slider-arrow { position: absolute; top: 124px; width: 28px; height: 30px; background: #8e9094; display: flex; align-items: center; justify-content: center; }
  .slider-arrow.prev { left: -3px; }
  .slider-arrow.next { right: -3px; }

  /* People */
  .person { position: absolute; left: 127px; width: 636px; height: 180px; }
  .person-title { font-size: 12.5px; font-weight: 400; line-height: 16px; color: var(--blue-text); padding-bottom: 2px; border-bottom: 1px solid var(--rule); }
  .person-photo { position: absolute; left: 0; top: 26px; width: 138px; height: 152px; background: var(--white); border: 1px solid #d9dbde; box-shadow: 0 6px 6px -4px rgba(0,0,0,.25); padding: 3px; }
  .person-photo div { width: 100%; height: 100%; }
  .person-body { position: absolute; left: 152px; top: 28px; width: 486px; height: 130px; }
  .person-intro { font-family: "Lato", sans-serif; font-size: 8.6px; line-height: 11px; color: #333; }
  .person-facts { position: absolute; left: 0; top: 39px; width: 100%; height: 60px; font-size: 8.6px; }
  .fact { position: absolute; display: flex; }
  .fact dt { color: var(--blue-text); font-size: 10px; width: 54px; }
  .fact dd { padding-top: 1px; color: #333; }
  .btn-message { position: absolute; left: 0; top: 106px; width: 112px; height: 22px; border-radius: 3px; border: 1px solid #155c94;
    background: linear-gradient(#2f8fd8, #1e76bb); color: var(--white); font-size: 10px; display: flex; align-items: center; }
  .btn-message span { flex: 1; padding-left: 8px; }
  .btn-message i { width: 20px; height: 100%; border-left: 1px solid #155c94; display: flex; align-items: center; justify-content: center; }

  /* Footer */
  .site-footer { position: absolute; left: 0; top: 1027px; width: 891px; height: 143px; background: var(--blue); border-top: 2px solid #c9d3dc; color: var(--white); }
  .footer-col { position: absolute; top: 29px; }
  .footer-col h3 { font-family: "Cinzel", serif; font-weight: 400; font-size: 11px; line-height: 14px; letter-spacing: .3px; white-space: nowrap; padding-bottom: 8px; border-bottom: 1px dotted rgba(255,255,255,.6); margin-bottom: 7px; }
  .footer-divider { position: absolute; top: 18px; width: 1px; height: 100px; background: rgba(0,0,0,.12); box-shadow: 1px 0 0 rgba(255,255,255,.12); }
  .quick-links { list-style: none; font-size: 8.5px; line-height: 12px; white-space: nowrap; }
  .quick-links li { height: 19px; }
  .quick-links li::before { content: "›"; margin-right: 6px; }
  .contact-line { display: flex; gap: 10px; font-size: 8.5px; line-height: 14px; margin-bottom: 6px; white-space: nowrap; }
  .contact-line svg { flex: none; width: 12px; margin-top: 1px; }
  .map-area { width: 154px; height: 64px; background: linear-gradient(135deg, #e8e3d6, #d9d6cc 60%, #efe6b8); border: 2px solid var(--white); }
  .footer-brand { position: absolute; left: 634px; top: 52px; display: flex; align-items: center; gap: 8px; }
  .footer-brand .brand-dot { width: 34px; height: 34px; background: rgba(255,255,255,.75); }
  .footer-brand .brand-name { font-size: 16px; line-height: 19px; color: var(--white); }
  .bottom-bar { position: absolute; left: 0; top: 1170px; width: 891px; height: 30px; background: var(--bar); color: #e8e8e8; font-size: 9px; text-align: center; line-height: 30px; }
</style>
</head>
<body>
  <div class="top-bar"></div>

  <header>
    <div class="brand">
      <span class="brand-dot"></span>
      <span class="brand-name">BRIGHTFOLD<br>PARTNERS</span>
    </div>
    <div class="call">
      <svg width="22" height="22" viewBox="0 0 22 22"><circle cx="11" cy="11" r="10" fill="none" stroke="#3a8fd0" stroke-width="1.2"/><path d="M8 6c-1.5 1-1.5 3 0 6s3 4.5 5 4.5l1-1.5-2-1.5-1 1c-1-.5-2-2-2.3-3.3l1-.7-1-2.2z" fill="#3a8fd0"/></svg>
      <span class="call-label">Call Us Now:</span>
      <span class="call-number">123-456-7890</span>
    </div>
    <nav class="main-nav">
      <a href="#">Home</a>
      <a href="#">Our Services</a>
      <a href="#" class="active">People</a>
      <a href="#">Contact Us</a>
    </nav>
  </header>

  <section class="slider">
    <div class="slide-image" role="img" aria-label="Photo of a businessman's hand touching a rising line chart of small figures"></div>
    <div class="slide-caption">LORAM IPSUM DOLOR SIT AMET, CONSECTETUER ADIPISCING ELIT</div>
    <div class="slider-arrow prev"><svg width="10" height="14" viewBox="0 0 10 14"><path d="M8 1 2 7l6 6" fill="none" stroke="#fff" stroke-width="2.5"/></svg></div>
    <div class="slider-arrow next"><svg width="10" height="14" viewBox="0 0 10 14"><path d="m2 1 6 6-6 6" fill="none" stroke="#fff" stroke-width="2.5"/></svg></div>
  </section>

  <main>
    <article class="person" style="top:429px">
      <h2 class="person-title">Lorem Ipsum Sit</h2>
      <div class="person-photo"><div role="img" aria-label="Full-length photo of a consultant in a dark suit" style="background:linear-gradient(90deg,#a9b9b4,#6f7c80 40%,#3b4146 60%,#c5cfcc)"></div></div>
      <div class="person-body">
        <p class="person-intro">Lorem ipsum dolor sit amet, consectetuer adipiscing elit, sed diam nonummy nibh euismod tincidunt ut laoreet dolore magna aliquam erat volutpat.</p>
        <dl class="person-facts">
          <div class="fact" style="left:0;top:0"><dt>Current</dt><dd>Lorem ipsum dolor sit amet</dd></div>
          <div class="fact" style="left:0;top:24px"><dt>Previous</dt><dd>Lorem ipsum dolor</dd></div>
          <div class="fact" style="left:0;top:47px"><dt>Phone</dt><dd>123 - 456 - 7890</dd></div>
          <div class="fact" style="left:222px;top:0"><dt>Education</dt><dd>Lorem ipsum dolor sit amet</dd></div>
          <div class="fact" style="left:222px;top:24px"><dt>Email</dt><dd>lorem@brightfold-mail.com</dd></div>
        </dl>
        <a class="btn-message"><span>Send a message</span><i><svg width="6" height="8" viewBox="0 0 6 8"><path d="M0 0l6 4-6 4z" fill="#fff"/></svg></i></a>
      </div>
    </article>

    <article class="person" style="top:627px">
      <h2 class="person-title">Lorem Ipsum Sit</h2>
      <div class="person-photo"><div role="img" aria-label="Portrait photo of a consultant in a suit" style="background:linear-gradient(160deg,#eae6dc,#c9b7a3 45%,#2a3550 80%)"></div></div>
      <div class="person-body">
        <p class="person-intro">Lorem ipsum dolor sit amet, consectetuer adipiscing elit, sed diam nonummy nibh euismod tincidunt ut laoreet dolore magna aliquam erat volutpat.</p>
        <dl class="person-facts">
          <div class="fact" style="left:0;top:0"><dt>Current</dt><dd>Lorem ipsum dolor sit amet</dd></div>
          <div class="fact" style="left:0;top:24px"><dt>Previous</dt><dd>Lorem ipsum dolor</dd></div>
          <div class="fact" style="left:0;top:47px"><dt>Phone</dt><dd>123 - 456 - 7890</dd></div>
          <div class="fact" style="left:222px;top:0"><dt>Education</dt><dd>Lorem ipsum dolor sit amet</dd></div>
          <div class="fact" style="left:222px;top:24px"><dt>Email</dt><dd>lorem@brightfold-mail.com</dd></div>
        </dl>
        <a class="btn-message"><span>Send a message</span><i><svg width="6" height="8" viewBox="0 0 6 8"><path d="M0 0l6 4-6 4z" fill="#fff"/></svg></i></a>
      </div>
    </article>

    <article class="person" style="top:827px">
      <h2 class="person-title">Lorem Ipsum Sit</h2>
      <div class="person-photo"><div role="img" aria-label="Portrait photo of a smiling consultant in a suit" style="background:linear-gradient(170deg,#f4f4f4,#d8b79c 45%,#2d2f36 80%)"></div></div>
      <div class="person-body">
        <p class="person-intro">Lorem ipsum dolor sit amet, consectetuer adipiscing elit, sed diam nonummy nibh euismod tincidunt ut laoreet dolore magna aliquam erat volutpat.</p>
        <dl class="person-facts">
          <div class="fact" style="left:0;top:0"><dt>Current</dt><dd>Lorem ipsum dolor sit amet</dd></div>
          <div class="fact" style="left:0;top:24px"><dt>Previous</dt><dd>Lorem ipsum dolor</dd></div>
          <div class="fact" style="left:0;top:47px"><dt>Phone</dt><dd>123 - 456 - 7890</dd></div>
          <div class="fact" style="left:222px;top:0"><dt>Education</dt><dd>Lorem ipsum dolor sit amet</dd></div>
          <div class="fact" style="left:222px;top:24px"><dt>Email</dt><dd>lorem@brightfold-mail.com</dd></div>
        </dl>
        <a class="btn-message"><span>Send a message</span><i><svg width="6" height="8" viewBox="0 0 6 8"><path d="M0 0l6 4-6 4z" fill="#fff"/></svg></i></a>
      </div>
    </article>
  </main>

  <footer class="site-footer">
    <div class="footer-col" style="left:113px;width:82px">
      <h3>Quick Links</h3>
      <ul class="quick-links">
        <li>Home</li>
        <li>Our Services</li>
        <li>Lead Expert Profile</li>
        <li>Contact Us</li>
      </ul>
    </div>
    <span class="footer-divider" style="left:218px"></span>
    <div class="footer-col" style="left:243px;width:140px">
      <h3>Contact Information</h3>
      <div class="contact-line"><svg height="14" viewBox="0 0 12 14"><path d="M6 0a4.5 4.5 0 0 0-4.5 4.5C1.5 8 6 14 6 14s4.5-6 4.5-9.5A4.5 4.5 0 0 0 6 0zm0 6.3a1.8 1.8 0 1 1 0-3.6 1.8 1.8 0 0 1 0 3.6z" fill="#fff"/></svg><span>Lorem ipsum dolor sit amet,<br>consectetuer adipiscing elit</span></div>
      <div class="contact-line"><svg height="12" viewBox="0 0 12 12"><path d="M2.5 1c-1.5 1-1.6 3 .3 6s4 4.3 5.7 4l1.3-1.6-2.2-1.7-1.1 1C5.3 8.2 4.2 6.8 3.9 5.5l1.2-.7L4 2.3z" fill="#fff"/></svg><span>123456789</span></div>
      <div class="contact-line"><svg height="10" viewBox="0 0 12 9"><rect width="12" height="9" fill="#fff"/><path d="M0 0l6 5 6-5" fill="none" stroke="#2383cc" stroke-width="1.2"/></svg><span>info@brightfoldpartners.com</span></div>
    </div>
    <span class="footer-divider" style="left:405px"></span>
    <div class="footer-col" style="left:431px;width:154px">
      <h3>Location Map</h3>
      <div class="map-area" role="img" aria-label="Street map showing the office location"></div>
    </div>
    <span class="footer-divider" style="left:606px"></span>
    <div class="footer-brand">
      <span class="brand-dot"></span>
      <span class="brand-name">BRIGHTFOLD<br>PARTNERS</span>
    </div>
  </footer>

  <div class="bottom-bar">Copyright © 2014 Brightfold Partners &nbsp;|&nbsp;&nbsp; All Rights Reserved.</div>
</body>
</html>
```